Stationary for security company
BRAMLOCK GUARDING LTD
Project: Stationary for security company
Stationary for security company  - Security
Creative Brief
Professional
148 MORTWELL CRESCENT DUNSBY KENT TN8 4QP
info@bramlock-guarding.co.uk
I DON'T NEED ADDRESS ON BUSINESS CARDS, JUST ON THE LETTER HEADS PLEASE.
specialize in:- -CCTV SYSTEMS -INTRUDER ALARMS -INTERCOM SYSTEMS -ELECTRICAL INSTALLATIONS UNDERTAKEN
delwynparfitt delwynparfitt
#183 I was referring to the back design back option 3 but in blue and with out the text just logo in centre. Also could you do me a design for invoices too?
#183 Hello, thank you for your designs I like the idea you have in design #183. Could you remove the phone number from the logo itself and complete the bottom line. We don't really need a number on the logo as we will have it on the stationary itself! And also the back of the business card you have in the design in black could you do that in blue, I like the blue and remove the text writing from the back of the card, so we just have the logo on the back. One more thing could you add Facebook and Twitter to the front of the business card please. Kind regards Delwyn Parfitt

```html
<!DOCTYPE html>
<html lang="en">
<head>
<meta charset="utf-8">
<title>Bramlock Guarding Ltd – Business Card</title>
<link rel="stylesheet" href="https://fonts.googleapis.com/css2?family=Open+Sans:wght@400;600;800&display=swap">
<style>
  :root{
    --backdrop:#d9d9d9;
    --card:#ffffff;
    --brand-blue:#1f4fa8;
    --deep-blue:#163b85;
    --ink:#222222;
    --muted:#555555;
    --swoosh-grey:#c9ccd2;
  }
  *{box-sizing:border-box;margin:0;padding:0}
  html,body{width:1200px;height:878px;overflow:hidden}
  body{background:var(--backdrop);font-family:"Open Sans",Arial,sans-serif;color:var(--ink);position:relative}
  .card{position:absolute;top:285px;width:540px;height:309px;background:var(--card);box-shadow:0 2px 6px rgba(0,0,0,.12);overflow:hidden}
  .card--front{left:45px}
  .card--back{left:615px}

  .name-mark{display:flex;align-items:center;gap:8px}
  .name-mark__square{width:14px;height:14px;background:var(--brand-blue)}
  .name-mark__text{font-weight:800;color:var(--brand-blue);letter-spacing:.3px;white-space:nowrap}
  .card--front .name-mark{position:absolute;left:40px;top:48px}
  .card--front .name-mark__text{font-size:17px}
  .card--back .name-mark{position:absolute;left:50%;top:50%;transform:translate(-50%,-50%)}
  .card--back .name-mark__text{font-size:24px}
  .card--back .name-mark__square{width:20px;height:20px}

  .contact-list{position:absolute;left:40px;top:108px;list-style:none;font-size:11.5px;color:var(--muted);line-height:20px}
  .contact-list li{display:flex;align-items:center;gap:8px}
  .contact-list svg{width:11px;height:11px;fill:var(--ink)}

  .person{position:absolute;left:318px;top:138px}
  .person__name{font-size:17px;font-weight:400;color:var(--ink)}
  .person__role{font-size:11px;color:var(--muted);margin-top:1px}

  .social-list{position:absolute;left:318px;top:212px;list-style:none;font-size:11px;color:var(--muted);line-height:18px}
  .social-list li{display:flex;align-items:center;gap:7px}
  .social-list__dot{width:10px;height:10px;border-radius:50%;background:var(--brand-blue)}

  .swoosh{position:absolute;left:0;bottom:0;width:540px;height:309px}
</style>
</head>
<body>

<section class="card card--front" aria-label="Business card front">
  <div class="name-mark">
    <span class="name-mark__square"></span>
    <span class="name-mark__text">BRAMLOCK GUARDING LTD</span>
  </div>

  <ul class="contact-list">
    <li><svg viewBox="0 0 24 24"><path d="M6.6 10.8a15 15 0 0 0 6.6 6.6l2.2-2.2a1 1 0 0 1 1-.25 11.4 11.4 0 0 0 3.6.57 1 1 0 0 1 1 1V20a1 1 0 0 1-1 1A17 17 0 0 1 3 4a1 1 0 0 1 1-1h3.5a1 1 0 0 1 1 1c0 1.25.2 2.45.57 3.57a1 1 0 0 1-.25 1z"/></svg>01892 604 118</li>
    <li><svg viewBox="0 0 24 24"><path d="M6 2h12v6H6zM3 9h18a1 1 0 0 1 1 1v7h-4v5H6v-5H2v-7a1 1 0 0 1 1-1zm5 8v3h8v-3z"/></svg>01892 604 119</li>
    <li><svg viewBox="0 0 24 24"><path d="M2 5h20v14H2zm2 2v.5l8 5 8-5V7zm0 2.9V17h16V9.9l-8 5z"/></svg>delwyn@bramlock-guarding.co.uk</li>
  </ul>

  <div class="person">
    <p class="person__name">Delwyn Parfitt</p>
    <p class="person__role">Managing Director</p>
  </div>

  <ul class="social-list" aria-label="Social media">
    <li><span class="social-list__dot"></span>/bramlockguarding</li>
    <li><span class="social-list__dot"></span>@bramlockguard</li>
  </ul>

  <svg class="swoosh" viewBox="0 0 540 309" aria-hidden="true">
    <path d="M0,200 C150,262 330,290 540,270 L540,309 L0,309 Z" fill="var(--swoosh-grey)"/>
    <path d="M0,206 C150,266 330,292 540,276" fill="none" stroke="var(--ink)" stroke-width="3"/>
    <path d="M0,222 C140,276 320,300 540,288 L540,309 L0,309 Z" fill="var(--brand-blue)"/>
    <path d="M0,246 C120,288 300,306 540,300 L540,309 L0,309 Z" fill="var(--deep-blue)"/>
  </svg>
</section>

<section class="card card--back" aria-label="Business card back">
  <div class="name-mark">
    <span class="name-mark__square"></span>
    <span class="name-mark__text">BRAMLOCK GUARDING LTD</span>
  </div>
</section>

</body>
</html>
```